LINGERIE WEBSHOP - Velora casa

We are looking for design and layout design for our webshop. We are company that sells lingerie and other connected textile products liki payamas and etc..
Our website will have approx 500 different products within 2 main catogories Woman/Man) and approx. 10 subcategories
Here is what we expect form design:
-Color pallete should be black and white (if you wish you can add some accent color)
-we want to leave feeling to customers of good quality products towards to luxury
-UX should be simple. Feel free to suggest layout
-frontpage layout, product list layout, product description layout, blog layout
-responsive design, compatible with smartphone

Target Market(s)

woman buying for themself, man buying for woman

Industry/Entity Type

Lingerie

Logo Text

VELORA CASA

Number of Pages Required

4 page

Font styles to use
Sans Serif
Decorative

Requirements
Must have
• simple UX
Nice to have
• difference for sexy/luxury lingerie and daily/cozy lingerie
Should not have
• cheap feel, unreliable

```html
<!DOCTYPE html>
<html lang="en">
<head>
<meta charset="utf-8">
<title>Velora Casa – Lingerie</title>
<link href="https://fonts.googleapis.com/css2?family=Open+Sans:wght@300;400;600&display=swap" rel="stylesheet">
<style>
:root{
  --ink:#111;
  --text:#222;
  --muted:#8a8a8a;
  --faint:#b5b5b5;
  --line:#e3e3e3;
  --band:#f6f7f9;
  --star:#f5b800;
  --badge:#1f5bd8;
  --skin-a:#f4f0ee;
  --skin-b:#e7d5c9;
}
*{margin:0;padding:0;box-sizing:border-box}
html,body{width:667px;height:1200px;overflow:hidden;background:#fff}
body{position:relative;font-family:"Open Sans",Arial,sans-serif;color:var(--text)}
.abs{position:absolute}

/* header */
.brand{left:0;width:667px;top:3px;text-align:center;font-weight:300;font-size:19px;letter-spacing:1.5px;color:#333}
.header-icons{left:518px;top:5px;display:flex;gap:8px}
.header-icons svg{width:16px;height:16px;stroke:#333;fill:none;stroke-width:1.3}
.cart{position:relative}
.cart-count{position:absolute;right:-4px;top:-3px;width:8px;height:8px;border-radius:50%;background:var(--ink);color:#fff;font-size:5px;line-height:8px;text-align:center;font-weight:600}
.main-nav{top:38px;left:0;width:667px;height:10px;font-size:7px;color:var(--ink)}
.main-nav a{position:absolute;color:inherit;text-decoration:none;letter-spacing:.2px}
.breadcrumb-band{left:0;top:60px;width:667px;height:15px;background:var(--band)}
.breadcrumb{left:62px;top:63px;font-size:6px;color:var(--faint)}

/* sidebar */
.filter-title{left:62px;width:112px;font-size:7.5px;font-weight:600;color:var(--ink);border-bottom:1px solid var(--line);height:14px}
.filter-title span{position:absolute;right:0;top:0;color:var(--faint);font-weight:300}
.swatch{width:15px;height:15px;border-radius:50%;top:119px}
.size{width:14px;height:14px;border-radius:50%;background:#f1f1f1;top:177px;font-size:6px;line-height:14px;text-align:center;color:#777}
.tags{left:62px;top:233px;font-size:5.5px;color:#555;display:flex;gap:8px}
.side-promo{left:61px;top:260px;width:121px;height:162px;background:linear-gradient(180deg,#f3f1f0 0%,#e9e3de 40%,#2a2626 60%,#f3f1f0 100%)}

/* catalogue */
.catalog-title{left:202px;top:88px;font-size:11px;color:var(--ink)}
.sort{left:559px;top:95px;font-size:5.5px;color:#666}
.sort svg{width:6px;height:4px;margin-left:5px;stroke:#666;fill:none}
.card{width:121px;height:200px}
.card-photo{width:121px;height:162px;position:relative}
.tone-leopard{background:linear-gradient(180deg,var(--skin-a),var(--skin-b) 45%,#8a6f77 62%,var(--skin-b) 80%,var(--skin-a))}
.tone-pink{background:linear-gradient(180deg,var(--skin-a),var(--skin-b) 55%,#e0908a 78%,var(--skin-b))}
.tone-black{background:linear-gradient(180deg,var(--skin-a),var(--skin-b) 35%,#3a3434 60%,var(--skin-b) 85%,var(--skin-a))}
.tone-cream{background:linear-gradient(180deg,var(--skin-a),var(--skin-b) 30%,#f1ebe3 45%,#8f8d96 70%,var(--skin-b))}
.tone-wine{background:linear-gradient(180deg,var(--skin-a),#d7b9a8 30%,#6e2a3d 55%,var(--skin-b) 85%,var(--skin-a))}
.tone-slip{background:linear-gradient(180deg,var(--skin-a),#d9bba6 30%,#1e1b1c 50%,#2a2626 80%,var(--skin-a))}
.badge-new{position:absolute;left:6px;top:7px;background:var(--badge);color:#fff;font-size:4px;padding:1px 4px;border-radius:1px;letter-spacing:.2px}
.card-meta{text-align:center;margin-top:5px}
.card-category{font-size:5.5px;color:var(--faint);line-height:8px}
.card-stars{font-size:7px;color:var(--star);letter-spacing:.5px;line-height:9px}
.card-name{font-size:7px;color:var(--ink);line-height:10px}
.load-more{left:358px;top:957px;width:90px;height:18px;border:1px solid #777;font-size:6px;line-height:16px;text-align:center;color:#444}

/* footer */
.footer{left:0;top:1003px;width:667px;height:157px;background:var(--band)}
.footer-col{top:1034px}
.footer-col h4{font-size:8.4px;font-weight:600;color:#222;letter-spacing:.2px;margin-bottom:5px}
.footer-col li{list-style:none;font-size:6.6px;font-weight:300;color:#777;line-height:15.3px}
.newsletter-copy{font-size:6.5px;font-weight:300;color:#888;line-height:7.6px;width:119px;margin-top:1px}
.subscribe{left:482px;top:1094px;width:109px;height:14px;display:flex}
.subscribe-field{flex:1;background:#fff;border:1px solid #ddd;font-size:5px;color:#777;line-height:12px;padding-left:5px}
.subscribe-btn{width:37px;background:var(--ink);color:#fff;font-size:6px;font-weight:600;line-height:14px;text-align:center}
.social{top:1117px;width:16px;height:16px;border:1px solid #555;border-radius:50%;font-size:4px;line-height:14px;text-align:center;color:#333}
.copyright{left:63px;top:1174px;font-size:9.3px;font-weight:300;color:#444}
.pay{top:1171px;width:32px;height:19px;border-radius:2px;background:#eceef2;border:1px solid #d5d8de;font-size:5px;font-weight:600;color:#444;line-height:17px;text-align:center}
</style>
</head>
<body>

<header>
  <div class="abs brand">VELORA CASA</div>
  <div class="abs header-icons">
    <svg viewBox="0 0 16 16"><circle cx="7" cy="7" r="5"/><line x1="11" y1="11" x2="15" y2="15"/></svg>
    <div class="cart"><svg viewBox="0 0 16 16"><path d="M3 5h10l1 10H2z"/><path d="M5.5 5V4a2.5 2.5 0 0 1 5 0v1"/></svg><span class="cart-count">5</span></div>
    <svg viewBox="0 0 16 16"><circle cx="8" cy="5" r="3.2"/><path d="M2 15c0-3.5 2.7-5.5 6-5.5s6 2 6 5.5z"/></svg>
    <svg viewBox="0 0 16 16"><line x1="2" y1="4" x2="14" y2="4"/><line x1="2" y1="8" x2="14" y2="8"/><line x1="2" y1="12" x2="14" y2="12"/><circle cx="10" cy="4" r="1.5" fill="#fff"/><circle cx="5" cy="8" r="1.5" fill="#fff"/><circle cx="9" cy="12" r="1.5" fill="#fff"/></svg>
  </div>
  <nav class="abs main-nav">
    <a style="left:195px">HOME</a><a style="left:233px">SHOP</a><a style="left:270px">WOMEN</a><a style="left:315px">NEW COLLECTION</a><a style="left:392px">BLOG</a><a style="left:429px">CONTACT US</a>
  </nav>
</header>
<div class="abs breadcrumb-band"></div>
<div class="abs breadcrumb">Home / Shop</div>

<aside>
  <div class="abs filter-title" style="top:92px">COLOR<span>-</span></div>
  <div class="abs swatch" style="left:62px;background:#e52b14"></div>
  <div class="abs swatch" style="left:81px;background:#000"></div>
  <div class="abs swatch" style="left:100px;background:#0a14f0"></div>
  <div class="abs swatch" style="left:119px;background:#1ee61e"></div>
  <div class="abs swatch" style="left:138px;background:#808080"></div>
  <div class="abs swatch" style="left:157px;background:#ff8c00"></div>
  <div class="abs filter-title" style="top:150px">SIZE<span>-</span></div>
  <div class="abs size" style="left:62px">S</div>
  <div class="abs size" style="left:82px">M</div>
  <div class="abs size" style="left:101px">L</div>
  <div class="abs filter-title" style="top:208px">TAGS<span>-</span></div>
  <div class="abs tags"><span>Dress</span><span>Lingerie</span></div>
  <div class="abs side-promo" role="img" aria-label="Model wearing a black satin slip dress with lace trim"></div>
</aside>

<main>
  <h1 class="abs catalog-title" style="font-weight:400">Lingerie (24)</h1>
  <div class="abs sort">Best Selling<svg viewBox="0 0 6 4"><path d="M.5.5 3 3 5.5.5"/></svg></div>

  <!-- row 1 -->
  <div class="abs card" style="left:202px;top:120px"><div class="card-photo tone-leopard" role="img" aria-label="Model in a leopard print bra"><span class="badge-new">NEW</span></div><div class="card-meta"><div class="card-category">Category Name</div><div class="card-stars">★★★★★</div><div class="card-name">Product Name</div></div></div>
  <div class="abs card" style="left:342px;top:120px"><div class="card-photo tone-pink" role="img" aria-label="Model in pink lace briefs"></div><div class="card-meta"><div class="card-category">Category Name</div><div class="card-stars">★★★★★</div><div class="card-name">Product Name</div></div></div>
  <div class="abs card" style="left:482px;top:120px"><div class="card-photo tone-black" role="img" aria-label="Model in a black lace bodysuit"><span class="badge-new">NEW</span></div><div class="card-meta"><div class="card-category">Category Name</div><div class="card-stars">★★★★★</div><div class="card-name">Product Name</div></div></div>
  <!-- row 2 -->
  <div class="abs card" style="left:202px;top:329px"><div class="card-photo tone-cream" role="img" aria-label="Model in a cream bralette and grey lace briefs"><span class="badge-new">NEW</span></div><div class="card-meta"><div class="card-category">Category Name</div><div class="card-stars">★★★★★</div><div class="card-name">Product Name</div></div></div>
  <div class="abs card" style="left:342px;top:329px"><div class="card-photo tone-wine" role="img" aria-label="Model in a burgundy lace bodysuit"></div><div class="card-meta"><div class="card-category">Category Name</div><div class="card-stars">★★★★★</div><div class="card-name">Product Name</div></div></div>
  <div class="abs card" style="left:482px;top:329px"><div class="card-photo tone-slip" role="img" aria-label="Model in a black satin slip dress"><span class="badge-new">NEW</span></div><div class="card-meta"><div class="card-category">Category Name</div><div class="card-stars">★★★★★</div><div class="card-name">Product Name</div></div></div>
  <!-- row 3 -->
  <div class="abs card" style="left:202px;top:537px"><div class="card-photo tone-leopard" role="img" aria-label="Model in a leopard print bra"><span class="badge-new">NEW</span></div><div class="card-meta"><div class="card-category">Category Name</div><div class="card-stars">★★★★★</div><div class="card-name">Product Name</div></div></div>
  <div class="abs card" style="left:342px;top:537px"><div class="card-photo tone-pink" role="img" aria-label="Model in pink lace briefs"></div><div class="card-meta"><div class="card-category">Category Name</div><div class="card-stars">★★★★★</div><div class="card-name">Product Name</div></div></div>
  <div class="abs card" style="left:482px;top:537px"><div class="card-photo tone-black" role="img" aria-label="Model in a black lace bodysuit"><span class="badge-new">NEW</span></div><div class="card-meta"><div class="card-category">Category Name</div><div class="card-stars">★★★★★</div><div class="card-name">Product Name</div></div></div>
  <!-- row 4 -->
  <div class="abs card" style="left:202px;top:746px"><div class="card-photo tone-cream" role="img" aria-label="Model in a cream bralette and grey lace briefs"><span class="badge-new">NEW</span></div><div class="card-meta"><div class="card-category">Category Name</div><div class="card-stars">★★★★★</div><div class="card-name">Product Name</div></div></div>
  <div class="abs card" style="left:342px;top:746px"><div class="card-photo tone-wine" role="img" aria-label="Model in a burgundy lace bodysuit"></div><div class="card-meta"><div class="card-category">Category Name</div><div class="card-stars">★★★★★</div><div class="card-name">Product Name</div></div></div>
  <div class="abs card" style="left:482px;top:746px"><div class="card-photo tone-slip" role="img" aria-label="Model in a black satin slip dress"><span class="badge-new">NEW</span></div><div class="card-meta"><div class="card-category">Category Name</div><div class="card-stars">★★★★★</div><div class="card-name">Product Name</div></div></div>

  <div class="abs load-more">NO MORE PRODUCTS</div>
</main>

<footer>
  <div class="abs footer"></div>
  <div class="abs footer-col" style="left:62px"><h4>CATEGORIES</h4><ul><li>Category 1</li><li>Category 2</li><li>Category 3</li><li>Category 4</li><li>Category 5</li></ul></div>
  <div class="abs footer-col" style="left:201px"><h4>MY ACCOUNT</h4><ul><li>Orders</li><li>Compare</li><li>Wishlist</li><li>Login</li><li>Register</li></ul></div>
  <div class="abs footer-col" style="left:342px"><h4>CONTACT US</h4><ul><li>Lorem ipsum is dolor amet</li><li>(+1)123-456-789</li><li>info@example.com</li></ul></div>
  <div class="abs footer-col" style="left:481px"><h4>NEWSLETTER SIGNUP</h4><p class="newsletter-copy">Sign up for our e-mail and be the first who know our special offers! Further-more, we will give a 15% discount on the next order after you sign up.</p></div>
  <div class="abs subscribe"><div class="subscribe-field">Enter your email address</div><div class="subscribe-btn">JOIN US</div></div>
  <div class="abs social" style="left:481px">Lumo</div>
  <div class="abs social" style="left:506px">Pinta</div>
  <div class="abs social" style="left:531px">Nesto</div>
  <div class="abs social" style="left:556px">Kavi</div>
  <div class="abs copyright">© 2020 Velora Casa, LLC. ALL RIGHTS RESERVED.</div>
  <div class="abs pay" style="left:469px">Orbis</div>
  <div class="abs pay" style="left:503px">Cardo</div>
  <div class="abs pay" style="left:536px">Finly</div>
  <div class="abs pay" style="left:570px">Paynet</div>
</footer>

</body>
</html>
```